Innovation Company Business Card Design

I need to have my business card updated. The current card was designed when the company started 2.5 years ago and was a quick and dirty job.

I need a new card design that is more professional and has my updated company tag line.

I will include the old card's Corel Draw file, and EPS versions as examples of the current design. I will also include the company logo eps and corel version files.

The company pantone colour is pantone 1805 c (a dark red)

I want the design to convey the nature of our business as a strategic technology innovation company, but yet still be professional. We are funky vibey and work from an industrial style office in a vibey designer dominat part of town. Though are clients include large banks and corporate clients too.

The information that needs to be on the card is in attached word document (but doesn't have to be in this order or format)

Final version needs to be supplied in PNG preview, as well as PSD file format (or other editable file version) so that personal information on card can be easily edited and reprinted.

Target Market(s)

CEO's of small to medium size companies
Marketing Managers of large coporates
Account managers of Digital Agencies

Industry/Entity Type

Business

Requirements
Must have
• 86x54mm will be cut in rounded corner credit card size format (Except if you recommend otherwise in your design)
Nice to have
• Some kind of background transparency combined with the pantone colour that gives the card some dimension and depth. But no gradient fills please :-)
Should not have
• Basic gradient fills
• Clipart

```html
<!DOCTYPE html>
<html lang="en">
<head>
<meta charset="utf-8">
<title>Vantaloop Business Card</title>
<link href="https://fonts.googleapis.com/css2?family=Montserrat:wght@800&family=Comfortaa:wght@300;400&family=Arimo:wght@400&display=swap" rel="stylesheet">
<style>
  :root {
    --brand-red: #b5121b;
    --brand-red-deep: #9c0f17;
    --card-white: #f4f4f4;
    --ink: #2b2b2b;
    --stage: #e7e4e1;
  }
  * { margin: 0; padding: 0; box-sizing: border-box; }
  html, body { width: 1200px; height: 720px; overflow: hidden; background: var(--stage); }
  .stage {
    width: 1200px; height: 720px;
    display: flex; align-items: center; justify-content: center; gap: 48px;
  }
  .card {
    position: relative;
    width: 516px; height: 324px;
    border-radius: 22px;
    overflow: hidden;
    background: var(--card-white);
    box-shadow: 0 10px 30px rgba(0,0,0,0.18);
  }
  .card-shape { position: absolute; inset: 0; }
  .card-shape path { fill: var(--brand-red); }

  /* Front */
  .wordmark {
    position: absolute; left: 92px; top: 118px;
    font-family: "Montserrat", sans-serif; font-weight: 800;
    font-size: 62px; letter-spacing: -2px; line-height: 1;
    color: #fff;
  }
  .tagline {
    position: absolute; left: 250px; top: 184px;
    font-family: "Arimo", sans-serif; font-size: 17px;
    color: #fff;
  }

  /* Back */
  .identity {
    position: absolute; left: 40px; top: 70px;
    color: #fff;
  }
  .identity-mark {
    display: flex; align-items: center; gap: 12px;
    font-family: "Montserrat", sans-serif; font-weight: 800;
    font-size: 22px; letter-spacing: -0.5px;
  }
  .identity-mark .square { width: 46px; height: 46px; background: #fff; }
  .person-name {
    margin-top: 40px;
    font-family: "Comfortaa", sans-serif; font-weight: 400;
    font-size: 34px; line-height: 1;
  }
  .person-role {
    margin-top: 8px;
    font-family: "Comfortaa", sans-serif; font-weight: 300;
    font-size: 15px; letter-spacing: 4px;
  }
  .contact {
    position: absolute; left: 318px; top: 70px;
    font-family: "Arimo", sans-serif; color: var(--ink);
    list-style: none;
  }
  .contact li { font-size: 15px; line-height: 22px; }
  .contact .gap { height: 14px; }
  .contact .address { font-size: 9px; line-height: 12px; text-transform: uppercase; }
</style>
</head>
<body>
<main class="stage">
  <section class="card card-front" aria-label="Card front">
    <svg class="card-shape" viewBox="0 0 516 324" aria-hidden="true">
      <path d="M36 0 H472 V112 H494 V324 H36 V244 H22 V96 H36 Z"/>
    </svg>
    <div class="wordmark">Vantaloop</div>
    <div class="tagline">Strategic Innovation</div>
  </section>

  <section class="card card-back" aria-label="Card back">
    <svg class="card-shape" viewBox="0 0 516 324" aria-hidden="true">
      <path d="M0 0 H256 V40 H290 V324 H0 Z"/>
    </svg>
    <div class="identity">
      <div class="identity-mark"><span class="square"></span>Vantaloop</div>
      <div class="person-name">Daniel Mercer</div>
      <div class="person-role">Founder &amp; MD</div>
    </div>
    <ul class="contact">
      <li>0831554027</li>
      <li>010 555 4193</li>
      <li class="gap"></li>
      <li>www.vantaloop.com</li>
      <li>daniel@vantaloop.com</li>
      <li class="gap"></li>
      <li>Vantaloop (Pty) Ltd</li>
      <li class="address">Suite 12, 40 Foundry Lane</li>
      <li class="address">Millhaven, JHB, RSA</li>
    </ul>
  </section>
</main>
</body>
</html>
```